Brand Identity - Web and social media vegan challenge

Hello! We started by ouselves and need some huge help! :D We have a logo, a pack for our product and we need to put this together with web and social media design (with some colours and letters we have already used, but we are totally open to changes and suggestions!) We are a female founded business of vegan meals in Brazil, called Zorbelinhas, the aminoacid that produces serotonin, the hormone of happines! Our purpose is to create a sense that vegan and fitness food can be tasty and an act of self-care, and that with good habits people can improve and nourish their bodies and minds :) Our business model is to deliver the meals("marmitas") frozen weekly/monthly so people can subscribe for our service and always have food :) So the design should communicate, carefulness, energy, appetite and incetivate people to comeback ;P There goes the logo, some material we have used on social media and colors we have chosen according to the color we have for our plates/food pics ;) Lettering used: gill sans, blackout (midnight/sunrise/2am) and nexa bold.

Industry/Entity Type

Food Service

Coding

Coded - Design and coding required

Number of Pages Required

2 page

Font styles to use
Sans Serif

Requirements
Must have
• Landing page, menu, form for orders.
Nice to have
• color palette attached

```html
<!DOCTYPE html>
<html lang="pt">
<head>
<meta charset="utf-8">
<title>Zorbelinhas – Vegan Meals</title>
<link href="https://fonts.googleapis.com/css2?family=Montserrat:wght@400;600;700&family=Cabin:ital,wght@0,400;0,600;1,400&family=Lora:ital@1&display=swap" rel="stylesheet">
<style>
:root{
  --red:#c8200f;
  --teal:#6fcfbf;
  --teal-bg:#a9e7dd;
  --ink:#111;
  --text:#333;
  --muted:#555;
  --grey-bg:#ececec;
  --peach:#f8d8bd;
  --yellow:#fbfa4b;
  --orange:#f8b13e;
  --mint:#a7e2dc;
  --salmon:#f0ba91;
  --footer:#efefef;
  --white:#fff;
}
*{box-sizing:border-box;margin:0;padding:0}
html,body{width:1200px;height:3822px;overflow:hidden}
body{font-family:"Cabin",sans-serif;color:var(--text);background:var(--white);position:relative}
section,header,footer{position:absolute;left:0;width:1200px}
.abs{position:absolute}

/* header */
.site-header{top:0;height:178px;background:var(--white)}
.brand-mark{left:0;width:1200px;top:50px;text-align:center;font-family:"Montserrat",sans-serif;font-weight:700;font-size:30px;color:var(--ink)}
.main-nav{top:134px;left:0;width:1200px;display:flex;justify-content:center;gap:48px;font-family:"Montserrat",sans-serif;font-weight:600;font-size:14px;color:var(--ink)}
.main-nav .active{color:var(--red)}

/* hero */
.hero{top:178px;height:528px;background:var(--grey-bg)}
.hero-title{left:171px;top:140px;font-family:"Montserrat",sans-serif;font-weight:700;font-size:49px;line-height:60px;white-space:nowrap}
.hero-title .l1{color:var(--ink)}
.hero-title .l2{color:var(--red)}
.hero-title .l3{color:var(--teal)}
.ribbon{top:350px;height:38px;line-height:38px;color:var(--white);font-family:"Montserrat",sans-serif;font-weight:600;font-size:16px;text-align:center}
.ribbon.subscribe{left:176px;width:176px;background:var(--red);clip-path:polygon(0 0,100% 0,96% 50%,100% 100%,0 100%,6% 50%)}
.ribbon.gift{left:348px;width:180px;background:var(--teal);clip-path:polygon(0 0,94% 0,100% 50%,94% 100%,0 100%,4% 50%)}
.hero-photo{left:600px;top:90px;width:500px;height:330px;border-radius:40px;transform:rotate(-6deg);background:linear-gradient(90deg,#f4f1ea 0%,#f0ebe0 45%,#5a5530 55%,#3c3a22 100%);box-shadow:0 20px 30px rgba(0,0,0,.2)}

/* section titles */
.section-title{left:0;width:1200px;text-align:center;font-family:"Montserrat",sans-serif;font-weight:700;font-size:24px;line-height:30px;color:var(--ink)}
.leaf{left:574px;width:52px;height:28px}
.lead{left:300px;width:600px;text-align:center;font-size:13px;line-height:22px;color:var(--text)}

/* pricing */
.pricing{top:706px;height:810px;background:var(--teal-bg)}
.plan{font-family:"Cabin",sans-serif;text-align:center;box-shadow:0 6px 14px rgba(0,0,0,.12)}
.plan .name{font-size:24px;padding-top:40px}
.plan .units{font-weight:600;font-size:28px;margin-top:20px;color:var(--ink)}
.plan ul{list-style:none;text-align:left;margin:42px 0 0 30px;font-size:14px;line-height:30px}
.plan li::before{content:"✔";margin-right:14px;font-size:13px}
.plan .details{position:absolute;left:0;right:0;bottom:0;height:52px;line-height:52px;border-top:1px dashed rgba(0,0,0,.35);font-size:15px}
.plan-1{left:217px;top:300px;width:234px;height:362px;background:var(--peach)}
.plan-1 .name,.plan-3 .name{color:var(--red)}
.plan-2{left:451px;top:275px;width:285px;height:413px;background:var(--red);color:var(--white)}
.plan-2 .name{font-size:30px;padding-top:38px}
.plan-2 .units{color:var(--white);font-size:36px;margin-top:14px}
.plan-2 ul{font-size:16px;line-height:32px;margin-left:36px}
.plan-2 .details{border-color:rgba(255,255,255,.5);height:66px;line-height:66px;font-size:16px}
.plan-3{left:736px;top:300px;width:250px;height:362px;background:var(--yellow)}

/* steps */
.how{top:1516px;height:619px;background:var(--white)}
.step-line{top:267px;height:2px;background:#f1a99a}
.step-icon{top:216px;width:102px;height:102px;border-radius:50%}
.step-num{top:324px;width:220px;text-align:center;font-family:"Montserrat",sans-serif;font-weight:700;font-size:62px;color:#d4d4d4}
.step-name{top:404px;width:220px;text-align:center;font-family:"Montserrat",sans-serif;font-weight:600;font-size:14px;color:var(--ink);line-height:18px}
.step-text{width:220px;text-align:center;font-family:"Lora",serif;font-style:italic;font-size:12px;line-height:19px;color:var(--muted)}
.step-note{color:var(--red);font-size:10px;font-family:"Montserrat",sans-serif;font-style:normal}

/* menu */
.menu{top:2135px;height:719px;background:linear-gradient(90deg,#f8ece3,#f6e4d8 60%,#f2dccb)}
.order-form{top:250px;left:310px;height:40px;display:flex;align-items:center;gap:10px;font-family:"Lora",serif;font-style:italic;font-size:22px;color:var(--ink)}
.select{width:108px;height:36px;background:var(--white);border:1px solid #777;font-family:"Cabin",sans-serif;font-style:normal;font-size:14px;padding:8px;position:relative}
.select::after{content:"▾";position:absolute;right:8px;top:8px}
.qty{display:flex;height:36px;border:1px solid #777;background:var(--white);font-family:"Cabin",sans-serif;font-style:normal;font-size:15px}
.qty span{width:36px;text-align:center;line-height:34px;border-right:1px solid #777}
.qty span:last-child{border:0}
.btn{background:var(--red);color:var(--white);font-family:"Montserrat",sans-serif;font-weight:600;font-size:14px;text-align:center;border-radius:2px}
.order-form .btn{width:110px;height:34px;line-height:34px;margin-left:10px;font-style:normal}
.dish{top:340px;width:240px}
.dish-photo{position:absolute;left:0;top:0;width:240px;height:180px;border-radius:24px;background:linear-gradient(120deg,#f1eee8 0 40%,#7a3a2a 55%,#5a3b25)}
.price{position:absolute;top:-18px;width:44px;height:44px;background:var(--red);transform:rotate(45deg);border-radius:5px}
.price b{display:block;transform:rotate(-45deg);color:var(--white);font-size:12px;line-height:44px;text-align:center;font-family:"Montserrat",sans-serif}
.dish-name{position:absolute;top:200px;left:0;width:240px;text-align:center;font-family:"Montserrat",sans-serif;font-weight:700;font-size:14px;color:var(--ink)}
.dish-text{position:absolute;top:230px;left:0;width:240px;text-align:center;font-size:13px;line-height:20px;color:var(--muted)}

/* contact */
.contact{top:2854px;height:604px;background:var(--white)}
.field{background:var(--white);border:1px solid #555;font-size:11px;padding:8px 6px;color:var(--ink)}
.salad{right:-60px;top:250px;width:200px;height:340px;border-radius:170px 0 0 170px;background:radial-gradient(circle at 60% 50%,#d86a5a 0,#b9c77a 45%,#eef0e8 75%)}
.contact .btn{left:548px;top:484px;width:104px;height:46px;line-height:46px}

/* footer */
.site-footer{top:3458px;height:364px;background:var(--footer)}
.footer-brand{left:160px;top:120px;width:240px;text-align:center;font-family:"Montserrat",sans-serif;font-weight:700;font-size:26px;color:var(--ink)}
.col-title{top:68px;font-family:"Montserrat",sans-serif;font-weight:600;font-size:16px;color:var(--ink)}
.links{top:110px;left:456px;list-style:none;font-size:12px;line-height:25px;color:var(--ink)}
.info{left:606px;font-size:12px;line-height:16px;color:var(--ink);display:flex;gap:16px;align-items:flex-start}
.divider{top:60px;width:1px;height:230px;background:#d6d6d6}
.social{top:116px;left:870px;display:flex;gap:8px}
.social span{width:28px;height:28px;border-radius:50%;background:#1a1a1a}
.copyright{left:0;width:1200px;top:322px;text-align:center;font-size:13px;color:var(--muted)}
</style>
</head>
<body>

<header class="site-header">
  <div class="abs brand-mark">Zorbelinhas</div>
  <nav class="abs main-nav">
    <span class="active">HOME</span><span>VEGAN MEALS</span><span>HOW IT WORKS</span><span>ABOUT US</span><span>TESTIMONIALS</span><span>BLOG</span><span>CONTACT</span>
  </nav>
</header>

<section class="hero">
  <h1 class="abs hero-title"><span class="l1">Por voce</span><br><span class="l2">Pelo planeta</span><br><span class="l3">Pelos animais</span></h1>
  <div class="abs ribbon subscribe">Subscribe</div>
  <div class="abs ribbon gift">Give as a Gift</div>
  <div class="abs hero-photo" role="img" aria-label="Vegan meal tray with rice, grated carrot and cooked greens"></div>
</section>

<section class="pricing">
  <svg class="abs leaf" style="top:86px" viewBox="0 0 52 28"><path d="M24 26C10 26 2 16 2 4c12 0 22 8 22 22z" fill="#111"/><path d="M28 26C42 26 50 16 50 4 38 4 28 12 28 26z" fill="#111"/></svg>
  <h2 class="abs section-title" style="top:122px">PRICING PLANS</h2>
  <p class="abs lead" style="top:180px">At vero eos et accusamus et iusto odio dignissimos ducimus qui blanditiis praesentium voluptat um deleniti atque corrupti quos dolores et quas molestias excepturi sint occaecati cupiditate non provident, similique sunt in culpa qui officia deserunt mollitia animi, id est laboru</p>

  <div class="abs plan plan-1">
    <div class="name">Plan 1</div><div class="units">4 Units</div>
    <ul><li>Iusto odio dignissimos</li><li>Voluptatum deleniti</li><li>Omnis dolor repellendus</li><li>Repudiandae sint</li></ul>
    <div class="details">View Details &nbsp;»</div>
  </div>
  <div class="abs plan plan-2">
    <div class="name">Plan 2</div><div class="units">5 to 7 Units</div>
    <ul><li>Iusto odio dignissimos</li><li>Voluptatum deleniti</li><li>Omnis dolor repellendus</li><li>Repudiandae sint</li></ul>
    <div class="details">View Details &nbsp;»</div>
  </div>
  <div class="abs plan plan-3">
    <div class="name">Plan 3</div><div class="units">10 to 20 Units</div>
    <ul><li>Iusto odio dignissimos</li><li>Voluptatum deleniti</li><li>Omnis dolor repellendus</li><li>Repudiandae sint</li></ul>
    <div class="details">View Details &nbsp;»</div>
  </div>
</section>

<section class="how">
  <svg class="abs leaf" style="top:102px" viewBox="0 0 52 28"><path d="M24 26C10 26 2 16 2 4c12 0 22 8 22 22z" fill="#111"/><path d="M28 26C42 26 50 16 50 4 38 4 28 12 28 26z" fill="#111"/></svg>
  <h2 class="abs section-title" style="top:140px">HOW IT WORKS?</h2>

  <div class="abs step-line" style="left:313px;width:123px"></div>
  <div class="abs step-line" style="left:538px;width:119px"></div>
  <div class="abs step-line" style="left:759px;width:123px"></div>

  <div class="abs step-icon" style="left:211px;background:var(--orange)">
    <svg width="102" height="102" viewBox="0 0 102 102"><rect x="34" y="28" width="34" height="46" rx="3" fill="#fff" stroke="#111" stroke-width="2"/><path d="M40 40h22M40 50h22M40 60h16" stroke="#111" stroke-width="2"/></svg>
  </div>
  <div class="abs step-icon" style="left:436px;background:var(--red)">
    <svg width="102" height="102" viewBox="0 0 102 102"><circle cx="51" cy="52" r="20" fill="#fff" stroke="#111" stroke-width="2"/><circle cx="51" cy="52" r="11" fill="none" stroke="#111" stroke-width="2"/></svg>
  </div>
  <div class="abs step-icon" style="left:657px;background:var(--mint)">
    <svg width="102" height="102" viewBox="0 0 102 102"><rect x="30" y="34" width="42" height="28" rx="3" fill="#fff" stroke="#111" stroke-width="2"/><path d="M30 42h42" stroke="#111" stroke-width="4"/></svg>
  </div>
  <div class="abs step-icon" style="left:882px;background:var(--salmon)">
    <svg width="102" height="102" viewBox="0 0 102 102"><rect x="32" y="34" width="38" height="26" rx="5" fill="none" stroke="#fff" stroke-width="3"/><path d="M42 60l-4 9 11-9" fill="none" stroke="#fff" stroke-width="3" stroke-linejoin="round"/></svg>
  </div>

  <div class="abs step-num" style="left:152px">01</div>
  <div class="abs step-num" style="left:377px">02</div>
  <div class="abs step-num" style="left:598px">03</div>
  <div class="abs step-num" style="left:823px">04</div>

  <div class="abs step-name" style="left:152px">Choose the Plan</div>
  <div class="abs step-name" style="left:377px">Choose the Menu</div>
  <div class="abs step-name" style="left:598px">Payment</div>
  <div class="abs step-name" style="left:823px">Schedule delivery<br>with us by ConversaJá</div>

  <p class="abs step-text" style="left:152px;top:436px">At verolore eos et accusamtsto odiodilorgnissimos ducimusiudis reesentium loremos duclereu egnissimos docimuels.</p>
  <p class="abs step-text" style="left:377px;top:436px">At verolore eos et accusamtsto odiodilorgnissimos ducimusiudis reesentium loremos duclereu egnissimos docimuels.</p>
  <p class="abs step-text" style="left:598px;top:436px">At verolore eos et accusamtsto odiodilorgnissimos ducimusiudis reesentium loremos duclereu egnissimos docimuels.</p>
  <p class="abs step-text" style="left:823px;top:456px">At verolore eos et accusamtsto odiodilorgnissimos loducloeimus<br><span class="step-note">(Obs: schedule within the website)</span></p>
</section>

<section class="menu">
  <svg class="abs leaf" style="top:80px" viewBox="0 0 52 28"><path d="M24 26C10 26 2 16 2 4c12 0 22 8 22 22z" fill="#111"/><path d="M28 26C42 26 50 16 50 4 38 4 28 12 28 26z" fill="#111"/></svg>
  <h2 class="abs section-title" style="top:116px">OUR MENU</h2>
  <p class="abs lead" style="top:162px">At vero eos et accusamus et iusto odio dignissimos ducimus qui blanditiis praesentium voluptat um deleniti atque corrupti quos dolores et quas molestias excepturi sint occaecati cup.</p>

  <div class="abs order-form">
    <span>Choose Plate</span>
    <div class="select">1</div>
    <span style="margin-left:18px">Quantity</span>
    <div class="qty"><span>−</span><span>1</span><span>+</span></div>
    <div class="btn">SUBMIT</div>
  </div>

  <div class="abs dish" style="left:185px">
    <div class="dish-photo" role="img" aria-label="Tray of red bean stew with rice and carrot"></div>
    <div class="price" style="left:170px"><b>$29</b></div>
    <div class="dish-name">MEALS LOREMUS</div>
    <p class="dish-text">At verolore eos et accusamus et iissimos ducimus qui blanditiis praevoitunt.</p>
  </div>
  <div class="abs dish" style="left:480px">
    <div class="dish-photo" role="img" aria-label="Tray of rice, carrot and sautéed greens" style="background:linear-gradient(120deg,#f2efe9 0 45%,#4a4a28 60%,#35361e)"></div>
    <div class="price" style="left:170px"><b>$29</b></div>
    <div class="dish-name">MEALS LOREMUS</div>
    <p class="dish-text">At verolore eos et accusamus et iissimos ducimus qui blanditiis praevoitunt.</p>
  </div>
  <div class="abs dish" style="left:760px">
    <div class="dish-photo" role="img" aria-label="Plate of golden vegetable curry with greens" style="left:40px;width:170px;height:170px;border-radius:50%;background:radial-gradient(circle,#c9962f 0,#a77c2a 45%,#e9e9ec 62%)"></div>
    <div class="price" style="left:180px"><b>$29</b></div>
    <div class="dish-name">MEALS LOREMUS</div>
    <p class="dish-text">At verolore eos et accusamus et iissimos ducimus qui blanditiis praevoitunt.</p>
  </div>
</section>

<section class="contact">
  <div class="abs salad" role="img" aria-label="Bowl of fresh salad with strawberries"></div>
  <svg class="abs leaf" style="top:70px" viewBox="0 0 52 28"><path d="M24 26C10 26 2 16 2 4c12 0 22 8 22 22z" fill="#111"/><path d="M28 26C42 26 50 16 50 4 38 4 28 12 28 26z" fill="#111"/></svg>
  <h2 class="abs section-title" style="top:104px">CONTACT US</h2>
  <p class="abs lead" style="top:152px">At vero eos et accusamus et iusto odio dignissimos ducimus qui blanditiis praesentium voluptat um deleniti atque corrupti quos dolores et quas molestias excepturi sint occaecati cup.</p>

  <div class="abs field" style="left:301px;top:242px;width:302px;height:40px">Name</div>
  <div class="abs field" style="left:610px;top:242px;width:302px;height:40px">CPF</div>
  <div class="abs field" style="left:301px;top:293px;width:302px;height:40px">E-mail</div>
  <div class="abs field" style="left:610px;top:293px;width:302px;height:40px">Cellphone</div>
  <div class="abs field" style="left:301px;top:345px;width:611px;height:122px">Adress for delivery</div>
  <div class="abs btn">SUBMIT</div>
</section>

<footer class="site-footer">
  <div class="abs footer-brand">Zorbelinhas</div>
  <div class="abs divider" style="left:432px"></div>
  <div class="abs divider" style="left:562px"></div>
  <div class="abs divider" style="left:824px"></div>

  <div class="abs col-title" style="left:456px">LINKS</div>
  <ul class="abs links"><li>Home</li><li>About</li><li>How it Works</li><li>Blog</li><li>Testimonials</li><li>Contact</li></ul>

  <div class="abs col-title" style="left:606px">CONTACT US</div>
  <div class="abs info" style="top:112px">
    <svg width="16" height="22" viewBox="0 0 16 22"><path d="M8 1a7 7 0 0 0-7 7c0 5 7 13 7 13s7-8 7-13a7 7 0 0 0-7-7z" fill="none" stroke="#111" stroke-width="1.5"/><circle cx="8" cy="8" r="2.5" fill="#111"/></svg>
    <span>41 Rua das Palmeiras,<br>Vila Serena, Campo Alto</span>
  </div>
  <div class="abs info" style="top:164px">
    <svg width="18" height="18" viewBox="0 0 18 18"><path d="M4 1l3 4-2 2c1 3 3 5 6 6l2-2 4 3-2 3C8 17 1 10 1 3z" fill="none" stroke="#111" stroke-width="1.5"/></svg>
    <span>0 300 412 775 20<br>0 300 412 775 36</span>
  </div>
  <div class="abs info" style="top:218px">
    <svg width="20" height="14" viewBox="0 0 20 14"><rect x="1" y="1" width="18" height="12" fill="none" stroke="#111" stroke-width="1.5"/><path d="M1 1l9 7 9-7" fill="none" stroke="#111" stroke-width="1.5"/></svg>
    <span>ola@zorbelinhas.test<br>fundadora@zorbelinhas.test</span>
  </div>

  <div class="abs col-title" style="left:866px">FOLLOW US</div>
  <div class="abs social"><span></span><span></span><span></span><span></span></div>

  <div class="abs copyright">© 2019 All Rights Are Reserved.Terms of Use | Privacy Policy</div>
</footer>

</body>
</html>
```